Black Hair Stylist Business Card

Looking a for a business card for my hair styling business. Would like the card to be clean and giving our company a sophisticated look. I specialize in black hair styling including braids, sew ins and extensions. I have uploaded two versions of my logo, both are PNG files.

On the front of the card I would like my logo, name (Marisol Quenby), phone number (Will provide number to the winner, for now use a fake number) and the area I service which is Portland, OR.

On the back I would like a list of the different styles of hair I do.
Knotless Braids - Feeding Braids - Bohemian Braids - Extensions - Sew In - Crochet - Butterfly Locs - Twist

On the back I would also like to note I have great reviews. Would be nice to have 5 Stars Emojis - TressNook I may also provide a QR code to take customers to my TressNook Page.

PLEASE NOTE: Originally I upload 2 versions of our logo. Now that we've seen some options we've decided to go with the pink logo and a white/cream white background.

Target Market(s)

Black Men and Women

Industry/Entity Type

Hair Styling and Design

Contact Information for Business Card

Please refer to the Project Description for details.

Font styles to use
Serif
Sans Serif

Colors
E54698
E96AAD
F1A4CE
F9D9EA
FCEFF6
A7469A
B969AE
D3A5CF
EDDBEB
F8F0F9

Requirements
Must have
• Please refer to the Project Description for details.
Nice to have
• Easy to read and feels sophisticated.
Should not have
• Should not be too busy looking.

```html
<!DOCTYPE html>
<html lang="en">
<head>
<meta charset="utf-8">
<title>Seraphine Braids &amp; Extensions — Business Card</title>
<link href="https://fonts.googleapis.com/css2?family=Montserrat:wght@400;500;600;700&display=swap" rel="stylesheet">
<style>
  :root{
    --pink:#e8288f;
    --pink-mid:#e54698;
    --pink-soft:#e96aad;
    --purple:#a7469a;
    --purple-deep:#b0449f;
    --ink:#1d1d1f;
    --white:#ffffff;
    --backdrop:#b3b3b3;
  }
  *{box-sizing:border-box;margin:0;padding:0}
  html,body{width:1200px;height:900px;overflow:hidden}
  body{background:var(--backdrop);font-family:"Montserrat",sans-serif;position:relative}

  .card{position:absolute;width:640px;height:366px;border-radius:18px;overflow:hidden;
        box-shadow:0 6px 18px rgba(0,0,0,.18)}

  /* front */
  .card-front{left:60px;top:64px;background:var(--white)}
  .front-brand{position:absolute;left:44px;top:58px;color:var(--pink);font-weight:600;
               font-size:30px;line-height:1.2;letter-spacing:.5px}
  .front-brand .brand-sub{display:block;font-size:30px}
  .brand-dot{position:absolute;left:44px;top:36px;width:14px;height:14px;border-radius:50%;background:var(--purple)}
  .holder{position:absolute;right:58px;top:150px;text-align:right}
  .holder-name{color:var(--pink);font-weight:700;font-size:30px;line-height:1}
  .holder-role{color:var(--ink);font-size:13px;margin-top:6px}
  .divider{position:absolute;left:40px;right:44px;top:212px;height:1.5px;background:var(--pink)}
  .contacts{position:absolute;left:44px;top:226px;list-style:none}
  .contacts li{display:flex;align-items:center;gap:12px;font-size:14.5px;color:var(--ink);height:27px}
  .contacts svg{width:16px;height:16px;flex:none}
  .area{position:absolute;right:58px;top:232px;font-size:15px;color:var(--ink)}
  .band-pink{position:absolute;left:0;right:0;bottom:0;height:10px;background:var(--pink)}
  .band-purple{position:absolute;right:0;bottom:0;width:250px;height:52px;background:var(--purple)}

  /* back */
  .card-back{left:500px;top:470px;
             background:linear-gradient(200deg,var(--purple-deep) 0%,var(--pink-mid) 55%,var(--pink) 100%)}
  .back-brand{position:absolute;left:0;right:0;top:60px;text-align:center;color:#f49ccb;
              font-weight:600;font-size:38px;line-height:1.15}
  .back-brand .brand-sub{display:block;font-size:22px;letter-spacing:3px}
  .services-title{position:absolute;left:0;right:0;top:190px;text-align:center;color:var(--white);
                  font-weight:700;font-size:21px}
  .services-title span{border-bottom:2px solid var(--white);padding-bottom:2px}
  .services{position:absolute;left:0;right:0;top:240px;text-align:center;color:var(--white);
            font-size:15.5px;line-height:34px;list-style:none}
  .services li{display:inline}
  .services li::before{content:"\2022";margin:0 8px 0 12px}
</style>
</head>
<body>

<section class="card card-front" aria-label="Business card front">
  <span class="brand-dot"></span>
  <div class="front-brand">Seraphine<span class="brand-sub">Braids &amp; Extensions</span></div>

  <div class="holder">
    <div class="holder-name">Marisol Quenby</div>
    <div class="holder-role">Owner</div>
  </div>

  <div class="divider"></div>

  <ul class="contacts">
    <li>
      <svg viewBox="0 0 16 16"><circle cx="8" cy="8" r="8" fill="#e8288f"/><path d="M5 4.5h2l.7 2-1.1.8a5 5 0 0 0 2.1 2.1l.8-1.1 2 .7v2c0 .5-.4.8-.9.8A6.5 6.5 0 0 1 4.2 5.4c0-.5.3-.9.8-.9z" fill="#fff"/></svg>
      555.214.7730
    </li>
    <li>
      <svg viewBox="0 0 16 16"><circle cx="8" cy="8" r="8" fill="#e8288f"/><rect x="4" y="5" width="8" height="6" rx="1" fill="#fff"/><path d="M4.3 5.4 8 8.3l3.7-2.9" stroke="#e8288f" stroke-width="1" fill="none"/></svg>
      hello@seraphinebraids.com
    </li>
    <li>
      <svg viewBox="0 0 16 16"><circle cx="8" cy="8" r="8" fill="#e8288f"/><circle cx="8" cy="8" r="4.2" fill="none" stroke="#fff" stroke-width="1.1"/><path d="M3.8 8h8.4M8 3.8c-2 2.4-2 6 0 8.4M8 3.8c2 2.4 2 6 0 8.4" stroke="#fff" stroke-width="1" fill="none"/></svg>
      www.seraphinebraids.com
    </li>
  </ul>

  <div class="area">Portland, OR</div>

  <div class="band-pink"></div>
  <div class="band-purple"></div>
</section>

<section class="card card-back" aria-label="Business card back">
  <div class="back-brand">Seraphine<span class="brand-sub">BRAIDS &amp; EXTENSIONS</span></div>
  <h2 class="services-title"><span>Our Services</span></h2>
  <ul class="services">
    <li>Knotless Braids</li><li>Feeding Braids</li><li>Bohemian Braids</li><li>Extensions</li><br>
    <li>Sew In</li><li>Butterfly Locs</li><li>Crochet</li><li>Twist</li>
  </ul>
</section>

</body>
</html>
```